Brookside Grocer

Hope all is well!

Wanted to make business cards for my father. His name is Faisal Qureshi and owns convenience stores. I have attached logo :)

He does not want any title just simple name and phone. An email would be nice as well.

Faisal Qureshi
Cell: 413-585-2046
Store: 413-719-4820

Brooksidegrocer512@fernpost.com

The design and style is totally up to you :) The colors we were looking for were the same as logo :)

```html
<!DOCTYPE html>
<html lang="en">
<head>
<meta charset="utf-8">
<title>Brookside Grocer – Business Cards</title>
<link rel="stylesheet" href="https://fonts.googleapis.com/css2?family=Montserrat:wght@400;500;700&display=swap">
<style>
  :root {
    --navy: #223474;
    --red: #ec2f3b;
    --white: #ffffff;
    --backdrop: #3b3b3d;
    --divider: rgba(255,255,255,0.35);
  }
  * { margin: 0; padding: 0; box-sizing: border-box; }
  html, body {
    width: 1200px; height: 1200px; overflow: hidden;
    background: var(--backdrop);
    font-family: "Montserrat", Arial, sans-serif;
  }
  .sheet {
    width: 1200px; height: 1200px;
    display: flex; flex-direction: column; align-items: center; justify-content: center;
    gap: 60px;
  }
  .card {
    position: relative;
    width: 900px; height: 514px;
    border-radius: 36px;
    overflow: hidden;
    box-shadow: 0 18px 40px rgba(0,0,0,0.45);
  }

  /* Front */
  .card-front { background: var(--white); }
  .front-top {
    position: absolute; left: 0; top: 0; width: 100%; height: 236px;
    display: flex; align-items: center; justify-content: center;
    padding-right: 120px;
  }
  .front-rule {
    position: absolute; left: 0; top: 236px; width: 100%; height: 8px;
    background: var(--red);
  }
  .front-bottom {
    position: absolute; left: 0; top: 258px; width: 100%; height: 256px;
    background: var(--navy);
    display: flex; align-items: center;
    padding-right: 56px;
  }
  .holder-name {
    width: 390px; flex: none; padding-left: 60px;
    color: var(--red); font-weight: 500; font-size: 30px; letter-spacing: 0.5px;
    text-transform: uppercase; white-space: nowrap;
  }
  .front-divider {
    width: 1px; height: 150px; background: var(--divider); flex: none;
  }
  .contact-list {
    list-style: none; padding-left: 36px; min-width: 0;
    color: var(--white); font-size: 19px; font-weight: 400;
    display: flex; flex-direction: column; gap: 12px;
  }
  .contact-list li { display: flex; align-items: center; gap: 12px; white-space: nowrap; }
  .contact-icon { width: 22px; height: 22px; flex: none; }

  /* Wordmark */
  .wordmark { display: flex; align-items: center; gap: 16px; }
  .wordmark-dot { width: 34px; height: 34px; border-radius: 50%; background: var(--red); flex: none; }
  .wordmark-name {
    font-weight: 700; font-size: 54px; letter-spacing: 1px; text-transform: uppercase;
    color: var(--navy); white-space: nowrap;
  }

  /* Back */
  .card-back {
    background: linear-gradient(120deg, #1f3070 0%, #2a3d80 45%, #1f2f6c 100%);
    display: flex; align-items: center; justify-content: center;
  }
  .card-back .wordmark-name { color: var(--white); font-size: 62px; }
  .card-back .wordmark-dot { width: 40px; height: 40px; }
</style>
</head>
<body>
<main class="sheet">
  <section class="card card-front" aria-label="Business card front">
    <div class="front-top">
      <div class="wordmark">
        <span class="wordmark-dot"></span>
        <span class="wordmark-name">Brookside Grocer</span>
      </div>
    </div>
    <div class="front-rule"></div>
    <div class="front-bottom">
      <p class="holder-name">Faisal Qureshi</p>
      <span class="front-divider"></span>
      <ul class="contact-list">
        <li>
          <svg class="contact-icon" viewBox="0 0 24 24" fill="none" stroke="#ec2f3b" stroke-width="2"><rect x="6" y="2" width="12" height="20" rx="2"/><line x1="11" y1="18.5" x2="13" y2="18.5"/></svg>
          413-585-2046
        </li>
        <li>
          <svg class="contact-icon" viewBox="0 0 24 24" fill="#ec2f3b"><path d="M6.6 10.8a15.1 15.1 0 0 0 6.6 6.6l2.2-2.2a1 1 0 0 1 1-.25 11.4 11.4 0 0 0 3.6.57 1 1 0 0 1 1 1V20a1 1 0 0 1-1 1A17 17 0 0 1 3 4a1 1 0 0 1 1-1h3.5a1 1 0 0 1 1 1c0 1.25.2 2.45.57 3.57a1 1 0 0 1-.25 1z"/></svg>
          413-719-4820
        </li>
        <li>
          <svg class="contact-icon" viewBox="0 0 24 24" fill="none" stroke="#ec2f3b" stroke-width="2"><rect x="2" y="5" width="20" height="14" rx="1"/><path d="M2 6l10 7 10-7"/></svg>
          brooksidegrocer512@fernpost.com
        </li>
      </ul>
    </div>
  </section>

  <section class="card card-back" aria-label="Business card back">
    <div class="wordmark">
      <span class="wordmark-dot"></span>
      <span class="wordmark-name">Brookside Grocer</span>
    </div>
  </section>
</main>
</body>
</html>
```